HRW / PFB

I need a business card for the owner of sister companies. Please see minimalist version of our old business card for just the Halvorsen business. We need to now have a card that shows off both the Halvorsen logo and the Pale Fern Builders logo. We would like the aesthetic to go well with our brand, and not differ greatly from our Halvorsen cards. These companies are sister companies, there is not one parent company. Looking for a visually appealing design, but not sure if it should be diagonal or something to make it visually attractive... or just some other type of divider. We prefer white logos with a blue background. White transparent background png logos are attached. Please use blue background with hex code 566b7c. The person and contact information will be on the back side, and I can do that myself. We will NOT need to add the text for design-build-sales-installation.

```html
<!DOCTYPE html>
<html lang="en">
<head>
<meta charset="utf-8">
<title>Halvorsen + Pale Fern Builders — Business Card</title>
<link rel="stylesheet" href="https://fonts.googleapis.com/css2?family=Montserrat:wght@400;500;700;800&display=swap">
<style>
  :root {
    --brand-blue: #566b7c;
    --paper: #ffffff;
    --ink: #1f2326;
    --stage: #e9e7e3;
  }
  * { box-sizing: border-box; margin: 0; padding: 0; }
  html, body {
    width: 1200px; height: 931px; overflow: hidden;
    background: var(--stage);
    font-family: "Montserrat", Arial, sans-serif;
  }
  .canvas { position: relative; width: 1200px; height: 931px; }

  .card {
    position: absolute;
    width: 620px; height: 354px;
    border-radius: 22px;
    overflow: hidden;
    box-shadow: 0 6px 18px rgba(0,0,0,0.12);
  }

  /* Front side: both sister brands */
  .card-front {
    left: 60px; top: 80px;
    background: var(--brand-blue);
    display: flex; align-items: center; justify-content: center;
  }
  .front-brand {
    width: 250px;
    display: flex; flex-direction: column; align-items: center;
    gap: 18px;
  }
  .front-mark { width: 56px; height: 56px; background: var(--paper); }
  .front-name {
    color: var(--paper);
    font-weight: 700;
    font-size: 28px;
    line-height: 1.15;
    text-align: center;
    text-transform: lowercase;
  }
  .front-divider {
    width: 2px; height: 170px;
    background: var(--paper);
    margin: 0 20px;
  }

  /* Back side: contact details */
  .card-back {
    left: 520px; top: 480px;
    background: var(--paper);
  }
  .back-band {
    position: absolute; left: 0; right: 0; bottom: 0; height: 26px;
    background: var(--brand-blue);
  }
  .back-logo {
    position: absolute; right: 44px; top: 48px;
    display: flex; align-items: center; gap: 14px;
  }
  .back-logo-mark { width: 46px; height: 46px; background: var(--brand-blue); }
  .back-logo-name {
    color: var(--brand-blue);
    font-weight: 700;
    font-size: 34px;
    text-transform: lowercase;
  }
  .person { position: absolute; left: 44px; top: 140px; }
  .person-name {
    color: var(--brand-blue);
    font-weight: 800;
    font-size: 28px;
    line-height: 1;
  }
  .person-role { color: var(--ink); font-size: 15px; margin-top: 6px; }
  .divider {
    position: absolute; left: 104px; right: 34px; top: 190px;
    height: 2px; background: var(--brand-blue);
  }
  .contact-list {
    position: absolute; left: 44px; top: 212px;
    list-style: none;
    display: flex; flex-direction: column; gap: 8px;
  }
  .contact-item {
    display: flex; align-items: center; gap: 12px;
    color: var(--ink); font-size: 15px;
  }
  .contact-icon { width: 16px; height: 16px; flex: none; }
  .address {
    position: absolute; right: 36px; top: 236px;
    text-align: right;
    color: var(--ink); font-size: 14px; line-height: 1.4;
  }
</style>
</head>
<body>
<main class="canvas">

  <section class="card card-front" aria-label="Card front">
    <div class="front-brand">
      <div class="front-mark"></div>
      <p class="front-name">halvorsen+co</p>
    </div>
    <div class="front-divider"></div>
    <div class="front-brand">
      <div class="front-mark"></div>
      <p class="front-name">pale fern<br>builders</p>
    </div>
  </section>

  <section class="card card-back" aria-label="Card back">
    <div class="back-logo">
      <div class="back-logo-mark"></div>
      <p class="back-logo-name">halvorsen+co</p>
    </div>

    <div class="person">
      <p class="person-name">Marcus Ellery</p>
      <p class="person-role">Owner</p>
    </div>
    <div class="divider"></div>

    <ul class="contact-list">
      <li class="contact-item">
        <svg class="contact-icon" viewBox="0 0 16 16" aria-hidden="true">
          <path fill="#566b7c" d="M3.5 1.5l2.3 2.6-1.2 1.7c.9 2 2.6 3.7 4.6 4.6l1.7-1.2 2.6 2.3-1.4 2.3C7.4 13.5 2.5 8.6 1.2 3z"/>
        </svg>
        (614)555-0187
      </li>
      <li class="contact-item">
        <svg class="contact-icon" viewBox="0 0 16 16" aria-hidden="true">
          <rect x="1" y="3" width="14" height="10" rx="1" fill="#566b7c"/>
          <path d="M1.5 4l6.5 5 6.5-5" fill="none" stroke="#fff" stroke-width="1.2"/>
        </svg>
        hello@halvorsenco.example
      </li>
      <li class="contact-item">
        <svg class="contact-icon" viewBox="0 0 16 16" aria-hidden="true">
          <circle cx="8" cy="8" r="7" fill="#566b7c"/>
          <path d="M1 8h14M8 1c-3 3.5-3 10.5 0 14M8 1c3 3.5 3 10.5 0 14" fill="none" stroke="#fff" stroke-width="1"/>
        </svg>
        www.halvorsenco.example
      </li>
    </ul>

    <p class="address">42 Alder Ridge Court<br>Westbrook, OH 43081 USA</p>

    <div class="back-band"></div>
  </section>

</main>
</body>
</html>
```